Business Card Design Project

Double sided business card - logo on one side, my details on the other.

I would like to see two options - my logo on a dark grey/black background and my logo on white.

My details as follows:

Trevan Moulsby MBus, FBQL
P: 0471 562 104
E: trevan@trevanmoulsby.com
W: www.trevanmoulsby.com

Target Market(s)

Managers in business, universities and government.

Industry/Entity Type

Business

Requirements
Must have
• Chirpex, Pagemuro and Vocanet icons

```html
<!DOCTYPE html>
<html lang="en">
<head>
<meta charset="utf-8">
<title>Trevan Moulsby – Business Card</title>
<link href="https://fonts.googleapis.com/css2?family=Oswald:wght@700&family=Arimo&family=Pathway+Gothic+One&display=swap" rel="stylesheet">
<style>
  :root {
    --card-grey: #5a5a5a;
    --card-edge: #3f3f3f;
    --panel-white: #f6f9fb;
    --accent-blue: #5b86e5;
    --label-blue: #33628f;
    --text-dark: #2f2f2f;
    --white: #ffffff;
  }
  html, body {
    margin: 0;
    padding: 0;
    width: 1002px;
    height: 1200px;
    overflow: hidden;
    background: var(--white);
  }
  .canvas {
    position: relative;
    width: 1002px;
    height: 1200px;
  }
  .card {
    position: absolute;
    left: 0;
    width: 1002px;
    box-sizing: border-box;
    border: 2px solid var(--card-edge);
    overflow: hidden;
  }
  .card--front {
    top: 0;
    height: 572px;
    background: var(--card-grey);
  }
  .brand-name {
    position: absolute;
    left: 126px;
    top: 200px;
    margin: 0;
    font-family: "Oswald", sans-serif;
    font-weight: 700;
    font-size: 104px;
    line-height: 1;
    letter-spacing: 0;
    color: var(--white);
    white-space: nowrap;
  }
  .tagline {
    position: absolute;
    left: 127px;
    top: 318px;
    margin: 0;
    font-family: "Arimo", sans-serif;
    font-size: 42px;
    line-height: 1;
    color: var(--white);
    white-space: nowrap;
  }
  .card--back {
    top: 626px;
    height: 574px;
    background: var(--card-grey);
  }
  .details-panel {
    position: absolute;
    left: 0;
    top: 0;
    width: 506px;
    height: 100%;
    background: var(--panel-white);
    border-right: 9px solid var(--accent-blue);
  }
  .details {
    list-style: none;
    margin: 0;
    padding: 0;
    position: absolute;
    left: 72px;
    top: 66px;
    font-family: "Pathway Gothic One", sans-serif;
    font-size: 42px;
    line-height: 1;
    color: var(--text-dark);
  }
  .details li {
    height: 101px;
    white-space: nowrap;
  }
  .details .person-name { color: var(--label-blue); }
  .details .label { color: var(--label-blue); }
  .social {
    position: absolute;
    left: 0;
    width: 506px;
    top: 458px;
    display: flex;
    justify-content: center;
    gap: 30px;
    font-family: "Pathway Gothic One", sans-serif;
    font-size: 32px;
    color: var(--label-blue);
  }
  .social-item {
    display: flex;
    align-items: center;
    gap: 9px;
  }
  .social-dot {
    width: 30px;
    height: 30px;
    background: var(--label-blue);
  }
</style>
</head>
<body>
<main class="canvas">
  <section class="card card--front" aria-label="Card front">
    <h1 class="brand-name">TREVANMOULSBY</h1>
    <p class="tagline">Business advice, research and training.</p>
  </section>

  <section class="card card--back" aria-label="Card back">
    <div class="details-panel">
      <ul class="details">
        <li class="person-name">Trevan Moulsby MBus, FBQL</li>
        <li><span class="label">P:</span> 0471 562 104</li>
        <li><span class="label">E:</span> trevan@trevanmoulsby.com</li>
        <li><span class="label">W:</span> www.trevanmoulsby.com</li>
      </ul>
      <div class="social">
        <span class="social-item"><span class="social-dot"></span>Pagemuro</span>
        <span class="social-item"><span class="social-dot"></span>Chirpex</span>
        <span class="social-item"><span class="social-dot"></span>Vocanet</span>
      </div>
    </div>
  </section>
</main>
</body>
</html>
```